Car finance company business card

Create a nice business card for our car financing company , Visit our website www.birchlanefinance.com for the phone number and idea of the company look. Please do not be afraid to be creative. Name on card Is Marc-Antoine Beaulieu and phone number is on our website adress of business is
27816 Boulevard Saint-Orvel,
Mirabel, QC K4R 2T8

```html
<!DOCTYPE html>
<html lang="fr">
<head>
<meta charset="utf-8">
<title>Birch Lane Finance – Business Card</title>
<link rel="stylesheet" href="https://fonts.googleapis.com/css2?family=Roboto:ital,wght@0,400;0,500;0,700;1,500&display=swap">
<style>
  :root {
    --backdrop: #2a2b2e;
    --card-white: #f3f3f4;
    --brand-blue: #2a2f9e;
    --brand-blue-light: #3a7fd6;
    --name-blue: #3c3aa0;
    --accent-orange: #e8661c;
    --text-dark: #3a3a3c;
    --white: #ffffff;
  }
  * { margin: 0; padding: 0; box-sizing: border-box; }
  html, body { width: 1200px; height: 1200px; overflow: hidden; }
  body {
    background: var(--backdrop);
    font-family: "Roboto", sans-serif;
    position: relative;
  }
  .card {
    position: absolute;
    left: 246px;
    width: 708px;
    height: 404px;
    border-radius: 18px;
    overflow: hidden;
  }
  .card--front { top: 166px; background: var(--card-white); }
  .card--back { top: 628px; background: var(--brand-blue); }

  .front-wave { position: absolute; left: 0; top: 0; width: 708px; height: 404px; }

  .mascot-art {
    position: absolute;
    left: 390px;
    top: 10px;
    width: 318px;
    height: 394px;
    border-radius: 46% 40% 0 0;
    background: radial-gradient(ellipse at 50% 35%, #f07a2a 0%, #e0621c 45%, #4b48a8 88%);
    opacity: 0.92;
  }

  .brand-lockup {
    position: absolute;
    display: flex;
    align-items: center;
    gap: 10px;
    color: var(--text-dark);
    font-weight: 700;
    text-transform: uppercase;
    white-space: nowrap;
  }
  .brand-lockup__dot {
    border-radius: 50%;
    background: var(--accent-orange);
    flex: none;
  }
  .card--front .brand-lockup { left: 50px; top: 90px; font-size: 22px; letter-spacing: 1px; }
  .card--front .brand-lockup__dot { width: 20px; height: 20px; }

  .contact-block { position: absolute; left: 50px; top: 172px; }
  .contact-block__name { font-size: 22px; font-weight: 500; color: var(--name-blue); line-height: 1.2; }
  .contact-block__role { font-size: 15px; color: var(--accent-orange); margin-top: 1px; }
  .contact-block__address { font-size: 16px; color: var(--text-dark); line-height: 1.3; margin-top: 22px; }
  .contact-list { list-style: none; margin-top: 10px; }
  .contact-list__item {
    display: flex; align-items: center; gap: 10px;
    font-size: 16px; color: var(--text-dark); line-height: 20px;
  }
  .contact-list__icon { width: 13px; height: 13px; flex: none; }

  .card--back .brand-lockup {
    left: 0; right: 0; top: 196px;
    justify-content: center;
    color: var(--white);
    font-size: 44px;
    letter-spacing: 2px;
  }
  .card--back .brand-lockup__dot { width: 34px; height: 34px; }
  .tagline {
    position: absolute; left: 0; right: 0; top: 348px;
    text-align: center;
    color: var(--white);
    font-size: 17px;
    font-style: italic;
    font-weight: 500;
  }
</style>
</head>
<body>

<section class="card card--front">
  <div class="mascot-art" role="img" aria-label="Large cartoon fox mascot in a blue suit giving a thumbs up and holding car keys"></div>

  <svg class="front-wave" viewBox="0 0 708 404" aria-hidden="true">
    <defs>
      <linearGradient id="waveGradient" x1="0" y1="0" x2="1" y2="0">
        <stop offset="0" stop-color="#2a45b0"/>
        <stop offset="1" stop-color="#2a2f9e"/>
      </linearGradient>
    </defs>
    <path d="M0 374 C300 370 520 342 708 284 L708 404 L0 404 Z" fill="url(#waveGradient)"/>
    <path d="M0 374 C300 370 520 342 708 284 L708 292 C520 350 300 376 0 380 Z" fill="var(--brand-blue-light)" opacity="0.6"/>
  </svg>

  <div class="brand-lockup">
    <span class="brand-lockup__dot"></span>
    <span class="brand-lockup__name">Birch Lane Finance</span>
  </div>

  <div class="contact-block">
    <p class="contact-block__name">Marc-Antoine Beaulieu</p>
    <p class="contact-block__role">Founder &amp; CEO</p>
    <p class="contact-block__address">27816 Boulevard Saint-Orvel<br>Mirabel, QC K4R 2T8</p>
    <ul class="contact-list">
      <li class="contact-list__item">
        <svg class="contact-list__icon" viewBox="0 0 16 16" aria-hidden="true"><path d="M3 1.5 L6 1.5 L7 5 L5 6.5 C6 9 7.5 10.5 9.5 11 L11 9 L14.5 10 L14.5 13 C14.5 14 13.5 14.5 12.5 14.5 C6.5 14 2 9.5 1.5 3.5 C1.5 2.5 2 1.5 3 1.5 Z" fill="var(--name-blue)"/></svg>
        (514) 555-0187
      </li>
      <li class="contact-list__item">
        <svg class="contact-list__icon" viewBox="0 0 16 16" aria-hidden="true"><rect x="1.5" y="3.5" width="13" height="9" fill="none" stroke="var(--name-blue)" stroke-width="1.4"/><path d="M1.5 3.5 L8 9 L14.5 3.5" fill="none" stroke="var(--name-blue)" stroke-width="1.4"/></svg>
        info@birchlanefinance.com
      </li>
      <li class="contact-list__item">
        <svg class="contact-list__icon" viewBox="0 0 16 16" aria-hidden="true"><circle cx="8" cy="8" r="6.5" fill="none" stroke="var(--name-blue)" stroke-width="1.3"/><ellipse cx="8" cy="8" rx="3" ry="6.5" fill="none" stroke="var(--name-blue)" stroke-width="1.1"/><path d="M1.5 8 H14.5 M2.5 4.8 H13.5 M2.5 11.2 H13.5" stroke="var(--name-blue)" stroke-width="1"/></svg>
        www.birchlanefinance.com
      </li>
    </ul>
  </div>
</section>

<section class="card card--back">
  <div class="brand-lockup">
    <span class="brand-lockup__dot"></span>
    <span class="brand-lockup__name">Birch Lane Finance</span>
  </div>
  <p class="tagline">Les spécialiste du financement automobile!</p>
</section>

</body>
</html>
```